黒の背景にムキムキの男性といったテイストではなく、清潔感のある優しいイメージでお願いいたします。
(イメージの参考)http://www.yukiura-dental.net/
表の面には陸上、サッカー、野球などのメジャースポーツの選手の写真を掲載して下さい。
【表面】・キャッチコピー・リード文・こんな方におすすめ・お客様の声
【裏面】・キャッチコピー・各商品の特徴・栄養士のプロフィール・料金プラン・申込の流れ
※詳細は添付ファイルをご確認下さいませ。
A4
両面
白を背景に、メインカラーはロゴと同じエメラルドグリーンでお願いいたします。
• 高解像度JPG (.jpg)
• イラストレーター形式 (.ai)
添付の写真素材もご利用下さいませ。
あまり時間もありませんので選定確約にいたします。
プロテインの価格は6,980円(税抜)に変更をお願いいたします。
プロテインの写真を撮り直しました。こちらをご利用下さいませ。
「私がサポートします!」のところの文章につきまして、「ジムストラクターも兼務」とありますが、正しくは「ジムインストラクターも兼務」でございます。申し訳ございませんがよろしくお願い致します。
また、プロテインはパッケージと出来上がりの写真と両方を掲載して頂けますと幸いです。どうぞよろしくお願い致します。
裏面の情報が少し多いと思いましたので、「私がサポートします!」などの部分は必要に応じて表面にレイアウトしてご提案頂いて結構でございます。何卒よろしくお願い致します。
「青嶺集成」Vol.71(http://www.seireishusei.com/cdrom/seireishusei.asp?vol=71)の素材は持っていますので、こちらの素材を使って頂いても結構です。仮で当て込んで頂ければ選定した際に該当する写真をお渡しいたします。外人さんはイメージと違いますのでお控え下さいませ。
栄養カウンセリングの価格が1,980円になっておりますが、正しくは1,750円(税抜)になります。申し訳ございませんがよろしくお願い致します。

全体的にスッキリしていて、雰囲気の優しい感じがイメージにぴったりでした。

ご提案頂きました皆様、ありがとうございました。どれもいいデザインで、選定はとても悩みました。
当選しなかった方には大変申し訳ございませんが、機会がございましたらまたお力添え頂けますと幸いです。

```html
<!DOCTYPE html>
<html lang="ja">
<head>
<meta charset="UTF-8">
<title>ヴェルダリス 栄養サポート</title>
<link rel="stylesheet" href="https://fonts.googleapis.com/css2?family=Noto+Sans+JP:wght@400;500;700;900&family=Dancing+Script:wght@600&family=Montserrat:wght@700;800&display=swap">
<style>
  :root{
    --emerald:#14a088;
    --emerald-deep:#0b8a74;
    --emerald-soft:#d8f1ec;
    --emerald-mist:#eef8f6;
    --ink:#3a3a3a;
    --muted:#6b6b6b;
    --paper:#ffffff;
  }
  *{margin:0;padding:0;box-sizing:border-box;}
  html,body{width:848px;height:1200px;overflow:hidden;background:var(--paper);}
  body{font-family:"Noto Sans JP",sans-serif;color:var(--ink);}
  .flyer{position:relative;width:848px;height:1200px;overflow:hidden;background:var(--paper);}

  .photo{position:absolute;}
  .runner-art{left:0;top:0;width:560px;height:470px;
    background:radial-gradient(ellipse at 40% 40%,#dff2ee 0%,#eef8f6 55%,rgba(255,255,255,0) 80%);}
  .product-photo{right:0;top:0;width:250px;height:210px;
    background:linear-gradient(160deg,#f3f6f5 0%,#dfe7e5 100%);}
  .product-label{position:absolute;right:18px;top:16px;text-align:right;font-family:"Montserrat",sans-serif;color:var(--emerald);line-height:1;}
  .product-label b{display:block;font-size:30px;font-weight:800;}
  .product-label span{display:block;font-size:12px;letter-spacing:4px;margin-top:4px;}
  .soccer-photo{right:0;top:222px;width:300px;height:240px;
    background:linear-gradient(180deg,#a9c7d8 0%,#d6e2e3 50%,#5f9a5a 100%);}
  .baseball-photo{left:618px;top:470px;width:112px;height:112px;border-radius:50%;
    background:radial-gradient(circle,#c9d7cf 0%,#7ea58b 100%);}
  .sprint-photo{right:0;top:540px;width:122px;height:100px;
    background:linear-gradient(180deg,#c3d6e4 0%,#8fa9b7 100%);}
  .track-photo{left:640px;top:630px;width:160px;height:110px;
    background:linear-gradient(180deg,#dbe6ec 0%,#b47b63 100%);}
  .cyclist-art{left:0;top:800px;width:380px;height:400px;
    background:radial-gradient(ellipse at 45% 55%,#dcefeb 0%,#eef8f6 55%,rgba(255,255,255,0) 80%);}
  .road-photo{right:0;bottom:0;width:470px;height:170px;
    background:linear-gradient(180deg,#cfdfe7 0%,#9fb3a6 60%,#7c8b80 100%);}

  .brand{position:absolute;left:26px;top:18px;display:flex;align-items:center;gap:8px;}
  .brand i{width:14px;height:14px;border-radius:50%;background:var(--emerald);}
  .brand span{font-weight:700;font-size:13px;letter-spacing:2px;color:var(--emerald);}

  .hero{position:absolute;left:62px;top:80px;width:600px;}
  .hero-tag{display:inline-block;background:var(--emerald);color:#fff;font-weight:700;font-size:18px;padding:3px 12px;}
  .hero-title{margin-top:8px;font-weight:900;font-size:46px;line-height:1.22;color:var(--emerald-deep);letter-spacing:1px;}
  .lead{position:absolute;left:196px;top:248px;width:370px;font-size:13px;line-height:1.95;color:var(--ink);}

  .section-script{font-family:"Dancing Script",cursive;color:var(--emerald);font-size:24px;line-height:1;}
  .section-title{font-weight:700;font-size:17px;color:var(--emerald-deep);margin-top:2px;}

  .recommend{position:absolute;left:60px;top:398px;width:480px;}
  .checklist{list-style:none;margin-top:8px;}
  .checklist li{display:flex;align-items:center;gap:8px;font-size:13px;line-height:1.9;}
  .checklist svg{flex:none;}

  .features{position:absolute;left:60px;top:552px;width:540px;}
  .features .section-title{font-size:18px;}
  .features .section-title em{font-style:normal;font-size:26px;color:var(--emerald);}
  .feature-list{list-style:none;margin-top:6px;counter-reset:f;}
  .feature-list li{counter-increment:f;font-size:13.5px;font-weight:500;line-height:1.85;}
  .feature-list li::before{content:counter(f) ". ";font-weight:700;color:var(--emerald-deep);}

  .voice{position:absolute;left:60px;top:722px;width:740px;}
  .voice-card{position:absolute;left:270px;top:32px;width:470px;border-top:2px solid var(--emerald);padding-top:10px;}
  .voice-head{display:flex;align-items:baseline;gap:12px;}
  .voice-head b{font-size:17px;color:var(--emerald-deep);}
  .voice-head span{font-size:12px;color:var(--muted);}
  .voice-quote{margin-top:6px;font-size:19px;font-weight:700;color:var(--emerald-deep);border-bottom:1px dashed var(--emerald);padding-bottom:6px;}
  .voice-body{margin-top:8px;font-size:10.5px;line-height:1.9;color:var(--ink);}
</style>
</head>
<body>
<main class="flyer">
  <div class="photo runner-art" role="img" aria-label="淡いグリーンで描かれた走る選手のシルエット"></div>
  <div class="photo product-photo" role="img" aria-label="プロテインのパッケージ写真">
    <div class="product-label"><b>WHEY<br>PROTEIN</b><span>ISOLATE</span></div>
  </div>
  <div class="photo soccer-photo" role="img" aria-label="ボールを蹴るサッカー選手の写真"></div>
  <div class="photo baseball-photo" role="img" aria-label="バットを構える野球選手の写真"></div>
  <div class="photo sprint-photo" role="img" aria-label="スタートを切る陸上選手の写真"></div>
  <div class="photo track-photo" role="img" aria-label="トラックを走るランナーの写真"></div>
  <div class="photo cyclist-art" role="img" aria-label="淡いグリーンで描かれた自転車選手のシルエット"></div>
  <div class="photo road-photo" role="img" aria-label="ロードバイクで走るサイクリストの写真"></div>

  <header class="brand"><i></i><span>VERDALIS</span></header>

  <section class="hero">
    <p class="hero-tag">現役スポーツ栄養士がサポート!</p>
    <h1 class="hero-title">自分専用の栄養で、<br>最高のパフォーマンスに</h1>
  </section>

  <p class="lead">自分にはどれくらいの栄養が必要なのか、ご存知ですか?必要な栄養は一人ひとり異なり、また同じ人でも時期によって異なります。食事は競技力を上げる上でもっとも大切な要素の一つ。数年後には大きな差となって現れます。たんぱく質やカルシウムなどの栄養不足を、後になって取り戻すことはできません。ヴェルダリスでは多くの栄養を必要とするアスリートを、スポーツ栄養士がマンツーマンでサポートします。</p>

  <section class="recommend">
    <p class="section-script">Recommended</p>
    <h2 class="section-title">こんな方におすすめ!</h2>
    <ul class="checklist">
      <li><svg width="14" height="14" viewBox="0 0 14 14"><rect x=".5" y=".5" width="13" height="13" fill="none" stroke="#14a088"/><path d="M3 7l3 3 5-6" fill="none" stroke="#14a088" stroke-width="1.8"/></svg>後半に競り勝つスタミナをつけたい</li>
      <li><svg width="14" height="14" viewBox="0 0 14 14"><rect x=".5" y=".5" width="13" height="13" fill="none" stroke="#14a088"/><path d="M3 7l3 3 5-6" fill="none" stroke="#14a088" stroke-width="1.8"/></svg>試合で100%のパフォーマンスを出したい</li>
      <li><svg width="14" height="14" viewBox="0 0 14 14"><rect x=".5" y=".5" width="13" height="13" fill="none" stroke="#14a088"/><path d="M3 7l3 3 5-6" fill="none" stroke="#14a088" stroke-width="1.8"/></svg>筋肉を落とさずに減量したい</li>
      <li><svg width="14" height="14" viewBox="0 0 14 14"><rect x=".5" y=".5" width="13" height="13" fill="none" stroke="#14a088"/><path d="M3 7l3 3 5-6" fill="none" stroke="#14a088" stroke-width="1.8"/></svg>当たり負けしない強い体を作りたい</li>
    </ul>
  </section>

  <section class="features">
    <p class="section-script">Four features</p>
    <h2 class="section-title">ヴェルダリスの栄養サポート<em>4</em>つの特徴</h2>
    <ol class="feature-list">
      <li>スポーツ栄養士のマンツーマン指導だから安心</li>
      <li>メールカウンセリングだから場所も予約なしで受けられる</li>
      <li>一人ひとりに合わせたオーダーメイドのサプリメント</li>
      <li>高品質で吸収率の高いオリジナルプロテイン</li>
    </ol>
  </section>

  <section class="voice">
    <p class="section-script">Customer's voice</p>
    <div class="voice-card">
      <div class="voice-head"><b>お客様の声</b><span>高森悠斗さん</span></div>
      <p class="voice-quote">300kmのレースの後でも筋肉痛になりませんでした</p>
      <p class="voice-body">趣味ではなく本気で走っているつもりでしたが、栄養のことはほとんど考えたことがありませんでした。カウンセリングで食事の記録を見てもらい、自分に足りないものがはっきり分かりました。専門家の意見をもとに補食のタイミングを変えただけで、長い距離を走った翌日の疲れ方がまるで違います。以前はレース後に何日も脚が重かったのに、今では翌日から普通に練習できています。サプリメントやプロテインも自分に合わせて選んでもらえるので、迷わず続けられるのが嬉しいです。</p>
    </div>
  </section>
</main>
</body>
</html>
```